Brightmoor Partners Branding Revamp

We are a consulting company, looking for a way to display and promote our brand. We have 2 sides to the business- Brightmoor (financial) and Partners (cyber security). The financial side products relate to business necessities: card processing, website design/hosting/maintenance, VoIP phone systems. The cyber security side promotes a bundled package of 4 solutions: network vulnerability scan, dark web scan, anti-ransomeware/malware software, and image-level backups. We want people to understand that partnering with Brightmoor Partners gives them “Assured Calm for Business” (tagline). Current badge and logos uploaded.

Target Market(s)

Small businesses

Contact Information for Business Card

Lena Marwick, Vice President, lena@brightmoorpartners.example, 555-806-1937, www.brightmoorpartners.example

Requirements
Nice to have
• I do prefer the darker background for front and back

```html
<!DOCTYPE html>
<html lang="en">
<head>
<meta charset="utf-8">
<title>Brightmoor Partners – Business Card</title>
<link rel="stylesheet" href="https://fonts.googleapis.com/css2?family=Montserrat:wght@400;500;700;800&display=swap">
<style>
  :root {
    --page: #ededed;
    --ink: #060607;
    --red: #e0262a;
    --red-dark: #8e0b0f;
    --tagline-ink: #1c1c1e;
    --white: #ffffff;
    --rule: #8a8a8a;
  }
  * { margin: 0; padding: 0; box-sizing: border-box; }
  html, body {
    width: 686px; height: 1200px; overflow: hidden;
    background: var(--page);
    font-family: "Montserrat", Arial, sans-serif;
  }
  .canvas { position: relative; width: 686px; height: 1200px; }

  .card {
    position: absolute; left: 63px; width: 560px; height: 320px;
    background: var(--ink); overflow: hidden;
    box-shadow: 0 14px 34px rgba(0,0,0,0.22);
  }
  .card--front { top: 260px; }
  .card--back  { top: 620px; }

  .card-art { position: absolute; inset: 0; width: 100%; height: 100%; }

  .texture {
    position: absolute;
    background: radial-gradient(ellipse at center, rgba(150,14,18,0.75) 0%, rgba(90,8,10,0.45) 45%, rgba(6,6,7,0) 75%);
  }
  .texture-clip {
    position: absolute; inset: 0; overflow: hidden;
    clip-path: polygon(0 0, 34.9% 0, 70.6% 100%, 0 100%);
  }
  .texture--front-top { left: -70px; top: -60px; width: 290px; height: 170px; }
  .texture--back-top  { left: -60px; top: -60px; width: 320px; height: 190px; }
  .texture--back-foot { right: -60px; bottom: -60px; width: 280px; height: 200px; opacity: .7; }

  .wordmark {
    position: absolute; text-align: center;
    color: var(--white); font-weight: 700;
  }
  .wordmark__dot {
    display: block; width: 12px; height: 12px; margin: 0 auto 10px;
    background: var(--red);
  }
  .wordmark__name { display: block; font-size: 18px; letter-spacing: 7px; line-height: 1; }
  .wordmark__sub  { display: block; font-size: 9px; letter-spacing: 3px; margin-top: 6px; line-height: 1; }
  .card--front .wordmark { left: 20px; width: 250px; top: 155px; }
  .card--back .wordmark  { left: 40px; width: 250px; top: 154px; }

  .site-link {
    position: absolute; left: 50px; top: 256px;
    color: var(--white); font-size: 9px; font-weight: 500; letter-spacing: 2.6px;
  }

  .tagline {
    position: absolute; left: 357px; top: 110px;
    color: var(--tagline-ink); font-weight: 800; font-size: 27px; line-height: 35px;
  }

  .divider {
    position: absolute; left: 278px; top: 115px; height: 125px;
    border-left: 1px dotted var(--rule);
  }
  .contact { position: absolute; left: 305px; top: 114px; color: var(--white); }
  .contact__name { color: var(--red); font-weight: 700; font-size: 19px; line-height: 22px; }
  .contact__role { font-size: 15px; font-weight: 500; line-height: 18px; }
  .contact__list { list-style: none; margin-top: 18px; }
  .contact__item {
    display: flex; align-items: center; gap: 8px;
    font-size: 12px; line-height: 24px;
  }
  .contact__icon { width: 9px; height: 9px; flex: none; }
</style>
</head>
<body>
<main class="canvas">

  <section class="card card--front" aria-label="Business card front">
    <svg class="card-art" viewBox="0 0 980 560" preserveAspectRatio="none" aria-hidden="true">
      <defs>
        <linearGradient id="paperTone" x1="0" y1="0" x2="1" y2="1">
          <stop offset="0" stop-color="#fafafa"/>
          <stop offset="0.5" stop-color="#eeeeef"/>
          <stop offset="1" stop-color="#e2e2e4"/>
        </linearGradient>
      </defs>
      <rect width="980" height="560" fill="url(#paperTone)"/>
      <polygon points="0,0 342,0 692,560 0,560" fill="#060607"/>
      <polygon points="362,95 410,95 672,560 630,560" fill="#e0262a"/>
      <polygon points="410,95 425,95 692,560 672,560" fill="#8e0b0f"/>
    </svg>
    <div class="texture-clip">
      <div class="texture texture--front-top" role="img" aria-label="Red low-poly network texture"></div>
    </div>

    <div class="wordmark">
      <span class="wordmark__dot"></span>
      <span class="wordmark__name">BRIGHTMOOR</span>
      <span class="wordmark__sub">PARTNERS</span>
    </div>
    <p class="site-link">www.brightmoorpartners.example</p>

    <h1 class="tagline">ASSURED<br>CALM FOR<br>BUSINESS</h1>
  </section>

  <section class="card card--back" aria-label="Business card back">
    <div class="texture texture--back-top" role="img" aria-label="Red low-poly network texture"></div>
    <div class="texture texture--back-foot" role="img" aria-label="Red low-poly network texture"></div>

    <div class="wordmark">
      <span class="wordmark__dot"></span>
      <span class="wordmark__name">BRIGHTMOOR</span>
      <span class="wordmark__sub">PARTNERS</span>
    </div>

    <div class="divider"></div>

    <div class="contact">
      <h2 class="contact__name">LENA MARWICK</h2>
      <p class="contact__role">Vice President</p>
      <ul class="contact__list">
        <li class="contact__item">
          <svg class="contact__icon" viewBox="0 0 10 10" aria-hidden="true"><path d="M2 0.5 L4 2.5 L3 3.8 C3.6 5 5 6.4 6.2 7 L7.5 6 L9.5 8 L8.3 9.5 C4.5 9.3 0.7 5.5 0.5 1.7 Z" fill="#e0262a"/></svg>
          555-806-1937
        </li>
        <li class="contact__item">
          <svg class="contact__icon" viewBox="0 0 10 10" aria-hidden="true"><rect x="0.5" y="2" width="9" height="6.5" fill="#e0262a"/><path d="M0.8 2.3 L5 5.6 L9.2 2.3" stroke="#060607" stroke-width="0.9" fill="none"/></svg>
          lena@brightmoorpartners.example
        </li>
        <li class="contact__item">
          <svg class="contact__icon" viewBox="0 0 10 10" aria-hidden="true"><g fill="none" stroke="#e0262a" stroke-width="0.9"><circle cx="5" cy="5" r="4.3"/><ellipse cx="5" cy="5" rx="1.9" ry="4.3"/><path d="M0.7 5 H9.3 M1.5 2.8 H8.5 M1.5 7.2 H8.5"/></g></svg>
          www.brightmoorpartners.example
        </li>
      </ul>
    </div>
  </section>

</main>
</body>
</html>
```